Design an Outstanding flyer for my company.

I need a flyer designed for our window tinting company based in Brisbane Queensland Australia. The flyer will be targeting Home tinting. We also do mobile car tinting. Something in regards to this could be incorporated into the flyer as well.
I want it to be 2 sided DL size. Black background.
It really needs to Pop, and be a real attention getter.
It needs to be easy to read.
I have provided a mock up with the info on it from our marketing company. It will need a spellcheck etc to make sure everything is correct.
Everything about it can be changed however you like.
I have also included the company logo.

Lets see what you've got!

Target Market(s)

Home Owners

Industry/Entity Type

Home Improvement

Font styles to use
Other font styles liked:
• Duan Penh

Requirements
Must have
• All the information on the mock up. Clear and easy to read.
• Must Stand Out!

```html
<!DOCTYPE html>
<html lang="en">
<head>
<meta charset="utf-8">
<title>BrightRay Window Tinting – Flyer</title>
<link rel="stylesheet" href="https://fonts.googleapis.com/css2?family=Cinzel:wght@400;500&display=swap">
<style>
  :root {
    --bg: #000000;
    --ink-light: #ffffff;
    --ink-dark: #111111;
    --gold: #e2b41c;
    --gold-deep: #a9780a;
    --silver-top: #f4f4f4;
    --silver-mid: #d6d6d6;
    --silver-low: #9d9d9d;
  }
  * { margin: 0; padding: 0; box-sizing: border-box; }
  html, body {
    width: 1200px;
    height: 2541px;
    overflow: hidden;
    background: var(--bg);
  }
  .flyer {
    position: relative;
    width: 1200px;
    height: 2541px;
    background: var(--bg);
    font-family: "Cinzel", "Times New Roman", serif;
    color: var(--ink-light);
    text-align: center;
  }
  .hero-art {
    position: absolute;
    left: 0;
    top: 0;
    width: 1200px;
    height: 870px;
    background:
      radial-gradient(ellipse 55% 60% at 48% 30%, rgba(226,180,28,0.75) 0%, rgba(169,120,10,0.35) 45%, rgba(0,0,0,0) 75%),
      radial-gradient(ellipse 30% 70% at 8% 40%, rgba(220,220,220,0.35) 0%, rgba(0,0,0,0) 70%),
      var(--bg);
  }
  .services {
    position: absolute;
    left: 0;
    top: 780px;
    width: 100%;
    font-size: 70px;
    line-height: 120px;
    letter-spacing: 0.5px;
  }
  .benefits {
    position: absolute;
    left: 128px;
    top: 1114px;
    width: 944px;
    height: 486px;
    background: linear-gradient(180deg, var(--silver-top) 0%, var(--silver-mid) 55%, var(--silver-low) 100%);
    color: var(--ink-dark);
    font-size: 76px;
    display: flex;
    flex-direction: column;
    justify-content: center;
    gap: 44px;
    line-height: 1;
  }
  .cta {
    position: absolute;
    left: 0;
    top: 1800px;
    width: 100%;
    font-size: 50px;
    line-height: 86px;
  }
  .contact {
    position: absolute;
    left: 0;
    top: 1975px;
    width: 100%;
    font-size: 45px;
    line-height: 62px;
  }
  .contact .web { text-transform: none; }
  .brand {
    position: absolute;
    left: 0;
    top: 2340px;
    width: 100%;
    display: flex;
    justify-content: center;
    align-items: center;
    gap: 26px;
  }
  .brand-dot {
    width: 78px;
    height: 78px;
    border-radius: 50%;
    background: var(--gold);
  }
  .brand-name {
    font-size: 76px;
    font-weight: 400;
    color: var(--gold);
    line-height: 1;
  }
</style>
</head>
<body>
  <main class="flyer">
    <div class="hero-art" role="img" aria-label="Large decorative gold star with sweeping white and grey road curves"></div>

    <h1 class="services">
      HOME WINDOW TINTING<br>
      MOBILE CAR TINTING
    </h1>

    <section class="benefits">
      <p>SAVE MONEY</p>
      <p>BLOCK 99.9% UV RAYS</p>
      <p>KEEP HEAT OUT</p>
    </section>

    <p class="cta">
      CALL BRISBANE’S LEADER IN<br>
      HOME WINDOW TINTING NOW!
    </p>

    <p class="contact">
      TEL : 07 3000 0148<br>
      SMS : 0400 000 271<br>
      <span class="web">www.brightraytinting.com.au</span>
    </p>

    <div class="brand">
      <span class="brand-dot"></span>
      <span class="brand-name">BrightRay</span>
    </div>
  </main>
</body>
</html>
```